Business Cards

Business card design for my company.
I would like the card's background colour to be black. You can also see our web site to get an idea of our brand. https://www.dlqmarrowfield.com.au/
- Name
- Email

```html
<!DOCTYPE html>
<html lang="en">
<head>
<meta charset="utf-8">
<title>DLQ Marrowfield – Business Card</title>
<link href="https://fonts.googleapis.com/css2?family=Poppins:wght@400;500;700&display=swap" rel="stylesheet">
<style>
  :root {
    --page-bg: #2a2b2e;
    --card-bg: #1e1f21;
    --card-edge: #141516;
    --green: #1f9a48;
    --white: #f2f2f2;
    --muted: #cfd0d2;
    --divider: #3a3c3f;
    --pattern: #252628;
  }
  * { box-sizing: border-box; margin: 0; padding: 0; }
  html, body { width: 1200px; height: 952px; overflow: hidden; }
  body {
    background: var(--page-bg);
    font-family: "Poppins", sans-serif;
    display: flex;
    flex-direction: column;
    align-items: center;
    justify-content: center;
    gap: 56px;
  }
  .card {
    width: 588px;
    height: 336px;
    background: var(--card-bg);
    box-shadow: 0 10px 30px rgba(0,0,0,.45), 0 0 0 1px var(--card-edge);
    position: relative;
    overflow: hidden;
  }
  /* Front */
  .card-front { display: flex; }
  .front-brand {
    width: 50%;
    display: flex;
    flex-direction: column;
    justify-content: center;
    align-items: center;
    padding: 0 24px;
  }
  .brand-mark {
    display: flex;
    align-items: center;
    gap: 10px;
    margin-top: 40px;
  }
  .brand-square { width: 14px; height: 14px; background: var(--green); }
  .brand-name {
    color: var(--white);
    font-weight: 700;
    font-size: 22px;
    letter-spacing: 2px;
    text-transform: uppercase;
  }
  .address {
    color: var(--muted);
    font-size: 11.5px;
    margin-top: 56px;
    text-align: center;
    line-height: 1.5;
  }
  .front-divider {
    width: 1px;
    background: var(--divider);
    margin: 70px 0 60px;
  }
  .front-contact {
    flex: 1;
    display: flex;
    flex-direction: column;
    justify-content: center;
    padding-left: 30px;
  }
  .person-name {
    color: var(--green);
    font-size: 21px;
    font-weight: 400;
    text-transform: uppercase;
    letter-spacing: .5px;
    line-height: 1.1;
  }
  .person-name strong { font-weight: 700; }
  .person-role { color: var(--white); font-size: 12px; margin: 4px 0 16px; }
  .contact-list { list-style: none; }
  .contact-list li {
    display: flex;
    align-items: center;
    gap: 8px;
    color: var(--muted);
    font-size: 11.5px;
    margin-bottom: 6px;
  }
  .contact-list svg { width: 12px; height: 12px; fill: var(--green); flex: none; }
  /* Back */
  .back-pattern { position: absolute; inset: 0; background: var(--pattern); }
  .back-brand {
    position: absolute;
    right: 70px;
    bottom: 80px;
    display: flex;
    align-items: center;
    gap: 8px;
  }
  .back-brand .brand-name { font-size: 14px; letter-spacing: 1.5px; }
  .back-brand .brand-square { width: 9px; height: 9px; }
</style>
</head>
<body>
  <section class="card card-front">
    <div class="front-brand">
      <div class="brand-mark">
        <span class="brand-square"></span>
        <span class="brand-name">DLQ Marrowfield</span>
      </div>
      <p class="address">1720 Larkspur Avenue Fairview, OR 97024</p>
    </div>
    <div class="front-divider"></div>
    <div class="front-contact">
      <h1 class="person-name">Martin E. <strong>Halloway</strong></h1>
      <p class="person-role">Managing Director</p>
      <ul class="contact-list">
        <li>
          <svg viewBox="0 0 24 24"><path d="M6.6 10.8a15.1 15.1 0 0 0 6.6 6.6l2.2-2.2a1 1 0 0 1 1-.25 11.4 11.4 0 0 0 3.6.57 1 1 0 0 1 1 1V20a1 1 0 0 1-1 1A17 17 0 0 1 3 4a1 1 0 0 1 1-1h3.5a1 1 0 0 1 1 1c0 1.25.2 2.45.57 3.57a1 1 0 0 1-.25 1z"/></svg>
          +00 987 654 32
        </li>
        <li>
          <svg viewBox="0 0 24 24"><path d="M2 5h20v14H2z M2 5l10 8 10-8" /></svg>
          hello@dlqmarrowfield.com.au
        </li>
        <li>
          <svg viewBox="0 0 24 24"><circle cx="12" cy="12" r="10"/></svg>
          www.dlqmarrowfield.com.au
        </li>
      </ul>
    </div>
  </section>

  <section class="card card-back">
    <div class="back-pattern" role="img" aria-label="Faint repeating brand monogram pattern across the card"></div>
    <div class="back-brand">
      <span class="brand-square"></span>
      <span class="brand-name">DLQ Marrowfield</span>
    </div>
  </section>
</body>
</html>
```